Either a trifold or double sided flyer/brochure

A flyer to help spark interest in a historic preservation project in Peterborough, NH--looking for something that captures the early 19th century rural village and mill times--American Primitive, Shaker, Cross Stitch Sampler...must be able to highlight home history as well as have all owners of house on a single page. Word document attached--can also provide files for the house painting, color photos, dunby photo, advertising photo or part of original settler map.
I like this brochure
http://tovabrenick.com/wordpress/pell-barn-museum-brochure/
community stakeholders, residents,
Historic Preservation, House Museums.

```html
<!DOCTYPE html>
<html lang="en">
<head>
<meta charset="utf-8">
<title>19th Century Rural Village and Mill Times</title>
<link rel="stylesheet" href="https://fonts.googleapis.com/css2?family=Arimo:wght@400;700&family=Bebas+Neue&family=Dancing+Script:wght@500&family=Libre+Baskerville&family=Poppins:wght@400;600&display=swap">
<style>
:root{
  --page:#e7e7e7;
  --parch-light:#dcc4a8;
  --parch-mid:#cdb091;
  --parch-dark:#b89070;
  --ink:#1f1213;
  --ink-soft:#2b1a1a;
  --red:#7a1114;
  --red-deep:#5a0c0e;
  --red-text:#8a1516;
  --rose:#eab8a6;
  --cream:#efe2d0;
  --text:#1b1414;
}
*{box-sizing:border-box;margin:0;padding:0}
html,body{width:1200px;height:1200px;overflow:hidden;background:var(--page)}
body{position:relative;font-family:Arimo,Arial,sans-serif;color:var(--text)}
.sheet{position:absolute;overflow:hidden;background:linear-gradient(90deg,var(--parch-mid),var(--parch-light) 40%,var(--parch-mid));box-shadow:0 6px 18px rgba(0,0,0,.18)}
.sheet--outside{left:238px;top:37px;width:728px;height:520px}
.sheet--inside{left:238px;top:619px;width:710px;height:515px}
.fold{position:absolute;top:0;bottom:0;width:1px;background:rgba(0,0,0,.12)}
.placeholder{position:absolute}
/* outside */
.band-dark{position:absolute;left:0;right:0;top:412px;bottom:0;background:var(--ink)}
.band-notch{position:absolute;left:662px;top:412px;width:66px;height:56px;background:var(--parch-light);border-bottom-left-radius:12px}
.red-square{position:absolute;left:672px;top:419px;width:44px;height:41px;border-radius:7px;background:var(--red)}
.section-head{position:absolute;left:0;display:flex;align-items:flex-start;gap:9px;color:var(--red-text);font-weight:700;font-size:13.5px;line-height:15px}
.section-head::before{content:"";display:block;width:54px;height:12px;background:var(--red);margin-top:1px}
.photo-frame{position:absolute;background:#c8a284;padding:10px}
.ad-block{position:absolute;left:243px;width:242px;top:431px;text-align:center;color:var(--cream)}
.ad-name{font-family:Poppins,sans-serif;font-weight:600;font-size:7.5px;letter-spacing:.5px}
.ad-trade{font-family:"Libre Baskerville",serif;font-size:8px;margin-top:2px}
.ad-small{font-family:Poppins,sans-serif;font-size:5px;margin-top:3px;line-height:6px;opacity:.9}
.ad-street{font-family:"Libre Baskerville",serif;font-size:7.5px;margin-top:3px}
.title-block{position:absolute;right:22px;top:108px;text-align:right;color:#fff}
.title-19{font-family:"Bebas Neue",sans-serif;font-size:62px;line-height:54px}
.title-19 sup{font-size:30px;vertical-align:top;line-height:30px}
.title-century{font-family:"Bebas Neue",sans-serif;font-size:62px;line-height:56px;letter-spacing:.5px}
.title-sub{font-size:19px;line-height:21px;margin-top:2px}
.tagline{position:absolute;right:81px;top:429px;text-align:right;color:var(--cream);font-size:15px;line-height:18px}
/* inside */
.history-card{position:absolute;left:15px;top:14px;width:214px;height:487px;border-radius:10px;background:linear-gradient(160deg,var(--red),var(--red-deep) 70%,#6e1012);padding:27px 12px 0 18px;color:var(--rose)}
.history-title{font-size:11.3px;line-height:13.5px}
.history-sub{font-size:9.4px;line-height:11px}
.history-body{margin-top:24px;font-size:7.9px;line-height:9.75px;text-align:justify}
.history-body p+p{margin-top:8px}
.story{position:absolute;left:255px;top:20px;width:198px;font-size:8px;line-height:9.8px;text-align:justify}
.story p+p{margin-top:13px}
.quote{position:absolute;left:255px;top:224px;width:198px;height:142px;border:1.2px dashed #222;padding:8px 6px 0 8px;font-family:"Dancing Script",cursive;font-size:8.6px;line-height:11.9px;text-align:justify}
.quote-mark{position:absolute;left:8px;top:-14px;font-family:Arimo,sans-serif;font-weight:700;font-size:48px;line-height:48px;background:var(--parch-light);padding:0 2px}
.quote p{text-indent:44px}
.story--end{top:386px}
.invite{position:absolute;left:473px;width:237px;text-align:center;font-weight:700}
.community-mark{position:absolute;left:581px;top:22px;width:27px;height:27px;border-radius:4px;background:#22325e}
.invite-lead{top:56px;font-size:9.3px}
.invite-name{top:71px;font-size:8.3px;line-height:10px}
.owners-label{position:absolute;left:506px;top:194px;width:162px;height:26px;background:var(--red);color:#f4d6c6;font-weight:700;font-size:8px;line-height:10px;text-align:center;padding-top:3px}
.owners{position:absolute;left:491px;top:228px;width:190px;display:flex;flex-direction:column;gap:2px}
.owner{display:flex;gap:3px;font-size:6.2px;line-height:7px}
.owner-name{flex:1;background:rgba(230,215,196,.75);padding:2px 4px 0 8px}
.owner-years{width:51px;background:var(--ink);color:#f1e4d6;border-radius:3px;display:flex;align-items:center;justify-content:center;font-weight:700;font-size:6.3px}
</style>
</head>
<body>

<section class="sheet sheet--outside">
  <div class="fold" style="left:243px"></div>
  <div class="fold" style="left:485px"></div>

  <div class="section-head" style="top:18px">Advertising<br>for the Ashcombe Mill</div>
  <div class="placeholder" role="img" aria-label="Photo of the yellow farmhouse and barn among autumn trees" style="left:19px;top:55px;width:211px;height:95px;background:linear-gradient(135deg,#3a2a18,#8a5a22 50%,#2a2214)"></div>
  <div class="placeholder" role="img" aria-label="Photo of the yellow farmhouse and barn in winter snow" style="left:19px;top:157px;width:211px;height:94px;background:linear-gradient(180deg,#5a4a3c,#b7a48a 55%,#e4dcd2)"></div>

  <div class="section-head" style="top:269px">Fred and Grace Dunby</div>
  <div class="band-dark"></div>
  <div class="band-notch"></div>
  <div class="red-square"></div>
  <div class="photo-frame" style="left:19px;top:297px;width:211px;height:199px">
    <div role="img" aria-label="Old sepia portrait of an elderly couple seated in their parlour" style="width:100%;height:100%;background:linear-gradient(160deg,#4a3a30,#2a201c 60%,#7a6a5a)"></div>
  </div>

  <div class="placeholder" role="img" aria-label="Sepia photo of the clapboard house gable with bare tree shadows" style="left:243px;top:0;width:242px;height:412px;background:linear-gradient(180deg,#3a302e,#7a6e6a 45%,#cfc6c2)"></div>
  <div class="placeholder" role="img" aria-label="Detail of the early settler lot map along the river" style="left:257px;top:213px;width:207px;height:179px;background:linear-gradient(135deg,#c9d0c6,#aab6ac);border:5px solid #e4e0da"></div>

  <div class="ad-block">
    <div class="ad-name">H. A. ASHCOMBE</div>
    <div class="ad-trade">Wool Carderr, Cloth Dresser</div>
    <div class="ad-name" style="font-size:5.5px;margin-top:2px">AND WOOL DYER</div>
    <div class="ad-small">GARMENTS of all KIND re-dyed. Dyes prepared for<br>family use, with direction for coloring.</div>
    <div class="ad-street">MILL LANE.</div>
    <div class="ad-small" style="margin-top:0">Peterboro', N.H. May 7, 1878.</div>
  </div>

  <div class="placeholder" role="img" aria-label="Photo of the yellow house gable against blue sky" style="left:606px;top:0;width:101px;height:53px;border-radius:0 0 9px 9px;background:linear-gradient(135deg,#1e3a6a,#c29a3a 60%,#8a6a2a)"></div>
  <svg class="placeholder" style="left:513px;top:68px" width="215" height="332" viewBox="0 0 215 332" role="img" aria-label="Close-up of cracked red painted door with iron latch">
    <defs><linearGradient id="redDoor" x1="0" y1="0" x2="1" y2="1"><stop offset="0" stop-color="#5a1214"/><stop offset=".5" stop-color="#3a0d0e"/><stop offset="1" stop-color="#1d0a0a"/></linearGradient></defs>
    <path d="M98 10 Q98 0 108 0 H215 V332 H100 Q90 332 90 322 V212 H10 Q0 212 0 202 V95 Q0 85 10 85 H86 Q98 85 98 73 Z" fill="url(#redDoor)"/>
  </svg>
  <div class="placeholder" role="img" aria-label="Photo of a narrow old staircase" style="left:532px;top:86px;width:55px;height:51px;border-radius:8px;background:linear-gradient(135deg,#d8c2a0,#6a4a2a)"></div>
  <div class="placeholder" role="img" aria-label="Close-up of worn green painted wood with an iron knob" style="left:533px;top:285px;width:104px;height:95px;border-radius:9px;background:linear-gradient(135deg,#3f7a6a,#2a5a4e 60%,#4a3a30)"></div>

  <div class="title-block">
    <div class="title-19">19<sup>TH</sup></div>
    <div class="title-century">CENTURY</div>
    <div class="title-sub">rural village and<br>mill times</div>
  </div>
  <div class="tagline">American Primitive,<br>Shaker, Cross Stitch<br>Sampler</div>
</section>

<section class="sheet sheet--inside">
  <div class="fold" style="left:236px"></div>
  <div class="fold" style="left:473px"></div>

  <article class="history-card">
    <div class="history-title">The Hartwell Homestead<br>History c. 1826</div>
    <div class="history-sub">Peterborough, New Hampshire</div>
    <div class="history-body">
      <p>In 1826, George S. Hartwell and his wife, Jane (Bramble) Hartwell purchased 26 acres from Robert Ashby on the Contoocook River, north of Pettingill's Woolen Mill in South Peterborough, NH. This parcel was carved out lot #32 which was comprised of 268 acres that were deeded to John Ashby (Robert Ashby's grandfather) by Jeremiah Tolland and John Crane on May 5, 1762. It is believed that Hartwell, who was blacksmith, built the house that currently stands at 47 Mill Lane in Peterborough, NH. He also built his forge on the site down by the river. It is likely that much of the forged hardware in the home was crafted by him. Feeling the need to leave Peterborough for a new frontier, Hartwell left town with his brother, Bowden, to purchase land in the emerging communities of Orleans County, NY. Before doing so, Hartwell sold the home, shop and buildings to Thomas Garland and his wife Alice (Pendleton) Garland in 1828.</p>
      <p>By trade, Thomas Garland was a cloth dresser and wool-carder. He was also a deeply religious man and served as deacon in the emerging, but still quite small, Baptist community. In those days, small groups of the Baptists and Methodists met in the Whitcomb Home for bible study, prayers and singing. The Whitcombs were well known abolitionists and their house served as a stop on the Underground Railroad. Deacon Garland died in 1839 and his estate was managed by Samuel Pendleton—very likely a relative of Alice—who protected Alice's dower. The property was then sold to Elijah Stone Ashcombe and his wife Achsah (Wetherby) Ashcombe</p>
    </div>
  </article>

  <div class="story">
    <p>Elijah was quite industrious and continued to expand the wool mill. He was an early investor in the Northfield Railroad and ceded a right of way to the railroad on the homestead. The mill eventually came under the control of his son, Henry A. Ashcombe, and operated until it burned down on April 20, 1874. Elijah passed away in 1877 and left the home to Mary Ellen Ashcombe who was most commonly known as “Ellen.”</p>
    <p>Ellen Ashcombe was approached in 1891 by Allie Pettingill, the owner of the Pettingill's Mill Complex, to ask if she would be willing to rent out the home to a couple from Boston. This turned out to be Marian and Edward Fairbrook, the founders of the Fairbrook Colony, who ended up spending their first summer in Peterborough, NH in the home. Marian recalls in her writings:</p>
  </div>

  <blockquote class="quote">
    <span class="quote-mark">“</span>
    <p>You can't fail to remember the two-story farmhouse almost across from the road from the iron bridge, now occupied by the Dunby Family. It had never been painted and was a lovely soft gray in color. There were really only four rooms and a kitchen, spotlessly clean and adequately furnished, which really didn't mean much but some chairs, tables and beds. Then in the kitchen was something that fascinated me, a stone bowl into which the clearest of water was all the time pouring and then running off into a a drain....</p>
  </blockquote>

  <div class="story story--end">
    <p>The Dunbys lived in this home for the longest time of any owner--and some refer to this area before the bridge, as Dunbys Corner. This moment of stewardship began under Fred Parker Dunby and his wife Grace E. (Sayer) Dunby around 1904 and lasted until 2015 when a descendant sold the home. The house is now under the stewardship of Edward M. Ferrante and Albert A. Holloway, Jr. and will be undergoing a significant restoration.</p>
  </div>

  <div class="community-mark"></div>
  <div class="invite invite-lead">They invite you to join their Homestead Circle group</div>
  <div class="invite invite-name">Hartwell Homestead c. 1826, Dunbys<br>Corner, Peterborough, New Hampshire</div>
  <div class="placeholder" role="img" aria-label="Folk painting of the white farmhouse and barn under a blue sky" style="left:481px;top:99px;width:213px;height:87px;border-radius:4px;background:linear-gradient(180deg,#3a4a78,#8a9ab8 45%,#2e4a2a)"></div>

  <div class="owners-label">Owners of 47 Mill Lane<br>Peterborough, New Hampshire</div>
  <div class="owners">
    <div class="owner" style="height:21px"><div class="owner-name">Robert Ashby (grandson of John Ashby) owned the land</div><div class="owner-years">1826</div></div>
    <div class="owner" style="height:21px"><div class="owner-name">George S. Hartwell and Jane (Bramble) Hartwell</div><div class="owner-years">1826-1828</div></div>
    <div class="owner" style="height:21px"><div class="owner-name">Deacon Thomas Garland and Alice (Pendleton) Garland (Baptist)</div><div class="owner-years">1828-1839</div></div>
    <div class="owner" style="height:29px"><div class="owner-name">Elijah Stone Ashcombe and Achsah (Wetherby) Ashcombe (mortgage between Samuel Pendleton and Ashcombe is 1845)</div><div class="owner-years">1839-1877</div></div>
    <div class="owner" style="height:13px"><div class="owner-name">Mary Ellen Ashcombe</div><div class="owner-years">1877-1898</div></div>
    <div class="owner" style="height:13px"><div class="owner-name">James Marlow</div><div class="owner-years">1898-1904</div></div>
    <div class="owner" style="height:21px"><div class="owner-name">Fred Parker Dunby and Grace E. (Sayer) Dunby</div><div class="owner-years">1904-1956</div></div>
    <div class="owner" style="height:29px"><div class="owner-name">Elinor (Dunby) Thornbury and Frank O Thornbury (Elinor was born in house on July 29, 1911)</div><div class="owner-years">1955-1998</div></div>
    <div class="owner" style="height:29px"><div class="owner-name">James H. Lindqvist and Maria Ruiz Lindqvist (James was nephew of Elinor (Dunby) Thornbury)</div><div class="owner-years">1998-2015</div></div>
    <div class="owner" style="height:13px"><div class="owner-name">Brookmere</div><div class="owner-years">2015-2022</div></div>
    <div class="owner" style="height:21px"><div class="owner-name">Edward M. Ferrante and Albert A. Holloway, Jr.</div><div class="owner-years">2022</div></div>
  </div>
</section>

</body>
</html>
```